Vormsted Off-Grid Energy

The company provides world wide installations and products for off-grid energy solutions. This means AC power where there is no network available. Mostly this is with solar panels combined with hybrid inverters and Lithium batteries. In the future small windmills and hydropower. The company is Dutch but has a hub in Hungary to supply the Balkan and surrounding countries.

We sell all Koru products and also Pinewatt and Lumask energy products

I have 3 versions of my logo. 2 attached and the third is the Off-grid energy text in black. Just see what works best with the design.
Obviously I need a good design but also good coding. It needs to meet al the latest (Google) search engine standards and should heave a web shop.
The web shop should be able to work with different currencies and calculate international shipping fees. Orders should be paid with; credit card, Quidflow, Fenpay or whatever is used internationally.

Coding

Number of Pages Required

5+ page

Font styles to use
Other font styles liked:
• see logo

Colors
0054AA
0677BA
7BADD7
CADEEF
E8F1F8
0094D4
00A9DD
6FCCEA
C7EBF8
E9F6FB
59FF00
82FF00
B8FF75
E3FFCB
F4FFEA
EB3D1F
EC4F4E
F09395
F8D3D4
FCEDEE

Requirements
Must have
• web shop
Nice to have
• slick design
Should not have
• stupid things ;-)

```html
<!DOCTYPE html>
<html lang="en">
<head>
<meta charset="utf-8">
<title>Vormsted Off-Grid Energy</title>
<link href="https://fonts.googleapis.com/css2?family=Michroma&family=Poppins:wght@400;500;600;700&display=swap" rel="stylesheet">
<style>
:root{
  --green:#8df25c;
  --green-soft:#b8ff75;
  --orange:#fa4616;
  --ink:#111111;
  --text:#555555;
  --muted:#888888;
  --line:#dddddd;
  --grey-bg:#f1f2f0;
  --dark:#1b1b1b;
  --white:#ffffff;
  --head:"Michroma",sans-serif;
  --body:"Poppins",sans-serif;
}
*{box-sizing:border-box;margin:0;padding:0}
html,body{width:1200px;height:4481px;overflow:hidden}
body{font-family:var(--body);color:var(--ink);background:var(--white);position:relative}
.abs{position:absolute}
h1,h2,h3,h4{font-family:var(--head);font-weight:400}
.btn{display:inline-flex;align-items:center;justify-content:center;font:600 13px var(--body);text-transform:uppercase;border-radius:4px;height:42px;padding:0 20px;text-decoration:none}
.btn-orange{background:var(--orange);color:var(--white)}
.btn-white{background:var(--white);color:var(--ink)}
.arrow-dot{width:44px;height:44px;border-radius:50%;background:var(--green);display:flex;align-items:center;justify-content:center}
.ph{border-radius:6px}

/* header */
.site-header{position:absolute;top:0;left:0;width:1200px;height:87px;background:var(--white)}
.brand{position:absolute;left:90px;top:24px;display:flex;align-items:center;gap:10px}
.brand-mark{width:26px;height:26px;background:var(--orange)}
.brand-name{font:700 20px var(--body);color:var(--ink)}
.main-nav a{position:absolute;top:34px;font:500 12px var(--body);color:var(--ink);text-decoration:none}
.main-nav a.active{color:var(--orange);font-weight:700}
.call{position:absolute;left:938px;top:24px;display:flex;gap:12px;align-items:center}
.call-icon{width:40px;height:40px;border-radius:50%;background:var(--orange);display:flex;align-items:center;justify-content:center}
.call small{display:block;color:var(--orange);font-size:9px;font-weight:600}
.call strong{font-size:17px;font-weight:700}

/* hero */
.hero{position:absolute;top:87px;left:0;width:1200px;height:668px;overflow:hidden}
.hero h1{position:absolute;left:90px;top:135px;font-size:56px;line-height:66px;color:var(--ink);letter-spacing:1px;-webkit-text-stroke:1.5px var(--ink)}
.hero p{position:absolute;left:90px;top:357px;width:450px;font-size:12.5px;line-height:21px;color:#222}
.hero .actions{position:absolute;left:90px;top:470px;display:flex;gap:12px}

/* brands */
.section-title{font-size:34px;text-align:center;letter-spacing:1px}
.brand-row{position:absolute;left:573px;width:473px;border-bottom:1px solid var(--line)}
.brand-row h3{font-size:22px;margin-bottom:12px}
.brand-row p{font-size:13.5px;line-height:22px;color:var(--text);width:370px}
.brand-row .arrow-dot{position:absolute;right:20px;top:38px;width:48px;height:48px}

/* solutions */
.solutions{position:absolute;top:1470px;left:0;width:1200px;height:516px;background:var(--grey-bg)}
.solution{position:absolute;top:165px;width:238px;height:292px;padding:22px 28px}
.solution.featured{background:var(--orange);border-radius:6px;color:var(--white)}
.solution .icon{width:80px;height:62px;border-radius:4px;margin-bottom:24px}
.solution h4{font-size:20px;line-height:25px;margin-bottom:18px}
.solution p{font-size:11px;line-height:20px;color:var(--text);margin-bottom:12px;height:60px;overflow:hidden}
.solution.featured p{color:var(--white)}
.solution .arrow-dot{width:30px;height:30px}
.solution.featured .arrow-dot{background:var(--white)}

/* why */
.why-item{position:absolute;left:126px;width:455px;height:86px;border-bottom:1px solid var(--line);display:flex;gap:18px;align-items:center;padding-left:12px}
.why-item:last-child{border-bottom:none}
.why-icon{width:52px;height:52px;flex:none}
.why-item h4{font-size:18px;margin-bottom:8px}
.why-item p{font-size:13px;color:var(--text)}

/* steps */
.step-num{position:absolute;width:108px;height:108px;border-radius:50%;background:var(--green);border:8px solid #d8fbc4;display:flex;align-items:center;justify-content:center;font:400 38px var(--head);color:var(--white)}
.step-text{position:absolute;width:200px;text-align:center}
.step-text h4{font-size:14px;line-height:19px;margin-bottom:8px}
.step-text p{font-size:12.5px;line-height:19px;color:var(--text)}

/* testimonials */
.review{position:absolute;top:3221px;width:414px;height:214px;border-radius:10px;background:var(--white);box-shadow:0 6px 24px rgba(0,0,0,.08);padding:28px 32px}
.review.featured{background:var(--orange);color:var(--white)}
.review .who{display:flex;align-items:center;gap:16px;margin-bottom:28px}
.review .avatar{width:68px;height:68px;border-radius:50%;background:#cfd4d8}
.review.featured .avatar{background:#ffb49b}
.review strong{font-size:15px;display:block;margin-bottom:4px}
.stars{color:#f6b400;font-size:16px;letter-spacing:1px}
.review p{font-size:13.5px;line-height:23px;color:var(--text)}
.review.featured p{color:var(--white)}
.dots{position:absolute;top:3471px;left:570px;display:flex;gap:6px}
.dots span{width:12px;height:12px;border-radius:50%;background:#cccccc}
.dots span:first-child{background:var(--green)}

/* contact */
.contact-card{position:absolute;left:169px;top:3622px;width:420px;height:491px;background:var(--green);border-radius:10px;padding:36px 42px;z-index:2}
.contact-card h2{font-size:27px;text-align:center;margin-bottom:26px}
.field{height:38px;background:var(--white);border-radius:3px;margin-bottom:12px;padding:12px 18px;font-size:11px;color:#555}
.field.tall{height:104px}
.submit{display:block;margin:24px auto 0;width:146px;height:42px;background:var(--orange);color:var(--white);border:0;border-radius:4px;font:600 13px var(--body)}

/* footer */
.site-footer{position:absolute;left:0;top:4043px;width:1200px;height:438px;background:var(--dark);color:#cccccc}
.footer-col{position:absolute;top:140px}
.footer-col h4{font-size:17px;color:var(--white);margin-bottom:22px}
.footer-col li{list-style:none;font-size:12.5px;margin-bottom:17px}
.footer-col li::before{content:"› ";color:var(--orange)}
.footer-col.info li::before{content:none}
.social{display:flex;gap:10px;margin-top:14px}
.social span{width:32px;height:32px;background:var(--orange);display:block}
.copyright{position:absolute;left:90px;right:90px;top:365px;border-top:1px solid #333;text-align:center;padding-top:24px;font-size:10px;color:var(--white)}
.to-top{position:absolute;left:1135px;top:368px;width:42px;height:42px;border-radius:50%;background:var(--orange);display:flex;align-items:center;justify-content:center}
</style>
</head>
<body>

<header class="site-header">
  <div class="brand"><span class="brand-mark"></span><span class="brand-name">Vormsted</span></div>
  <nav class="main-nav">
    <a class="active" style="left:592px">HOME</a>
    <a style="left:663px">About Us</a>
    <a style="left:751px">Products</a>
    <a style="left:839px">Contact Us</a>
  </nav>
  <div class="call">
    <span class="call-icon"><svg width="16" height="12" viewBox="0 0 16 12"><rect width="16" height="12" rx="1" fill="#fff"/><path d="M0 1l8 6 8-6" stroke="#fa4616" stroke-width="1.6" fill="none"/></svg></span>
    <div><small>CALL US</small><strong>+012 480 3917</strong></div>
  </div>
</header>

<section class="hero">
  <svg class="abs" style="left:0;top:0" width="1200" height="668" viewBox="0 0 1200 668">
    <rect width="1200" height="668" fill="#8df25c"/>
    <path d="M1110 0 C900 220 650 470 400 668 L1200 668 L1200 0 Z" fill="#fa4616"/>
    <path d="M1110 0 C900 220 650 470 400 668" stroke="#c8ff9e" stroke-width="6" fill="none" opacity=".6"/>
  </svg>
  <div class="abs ph" role="img" aria-label="Hybrid inverter, battery cabinet and solar charge controller product group" style="left:617px;top:62px;width:460px;height:548px;background:linear-gradient(160deg,#f4f4f4 0%,#dcdcdc 55%,#1a1a1a 78%,#1d7fd6 100%)"></div>
  <h1>Power<br>Anywhere,<br>Anytime</h1>
  <p>Take control of your energy needs with reliable off-grid power solutions. Whether you're in a remote location, need backup energy, or want to reduce dependence on the grid, we provide cutting-edge solar, hybrid inverter, and lithium battery solutions.</p>
  <div class="actions"><a class="btn btn-orange">Get a Quote</a><a class="btn btn-white">Learn More</a></div>
</section>

<section class="brands">
  <h2 class="section-title abs" style="top:895px;left:0;width:1200px">Our Premium Brands</h2>
  <div class="abs ph" role="img" aria-label="Inverter, batteries and cabinet from the premium brands" style="left:157px;top:950px;width:383px;height:440px;background:linear-gradient(150deg,#fde3d9 0%,#ececec 35%,#d6d6d6 60%,#222 85%,#1d7fd6 100%)"></div>
  <div class="brand-row" style="top:990px;height:130px">
    <h3>Koru</h3><p>Smart and powerful hybrid inverters and solar products designed for maximum efficiency and durability.</p>
    <span class="arrow-dot"><svg width="16" height="16"><path d="M3 13L13 3M6 3h7v7" stroke="#fff" stroke-width="1.8" fill="none"/></svg></span>
  </div>
  <div class="brand-row" style="top:1138px;height:102px">
    <h3>Pinewatt</h3><p>High-performance lithium batteries for long-lasting, stable energy storage.</p>
    <span class="arrow-dot" style="top:20px"><svg width="16" height="16"><path d="M3 13L13 3M6 3h7v7" stroke="#fff" stroke-width="1.8" fill="none"/></svg></span>
  </div>
  <div class="brand-row" style="top:1258px;height:110px;border-bottom:none">
    <h3>Lumask Energy</h3><p>Reliable inverters, battery chargers, and complete off-grid energy management systems.</p>
    <span class="arrow-dot" style="top:20px"><svg width="16" height="16"><path d="M3 13L13 3M6 3h7v7" stroke="#fff" stroke-width="1.8" fill="none"/></svg></span>
  </div>
</section>

<section class="solutions">
  <h2 class="abs" style="left:122px;top:70px;font-size:34px">Our Off-Grid Solutions</h2>
  <a class="btn btn-orange abs" style="left:910px;top:63px;height:48px">View All Product</a>
  <div class="solution" style="left:98px">
    <div class="icon" role="img" aria-label="Solar panel system" style="background:linear-gradient(#2f4a7a,#c9b28a)"></div>
    <h4>Solar Power Systems</h4><p>Harness the sun's energy for an independent, eco-friendly power supply.</p>
    <span class="arrow-dot"><svg width="12" height="12"><path d="M2 10L10 2M4 2h6v6" stroke="#fff" stroke-width="1.6" fill="none"/></svg></span>
  </div>
  <div class="solution featured" style="left:361px">
    <div class="icon" role="img" aria-label="Hybrid inverter" style="background:linear-gradient(#f0f0f0,#bfbfbf);width:50px"></div>
    <h4>Hybrid Inverters</h4><p>Seamlessly switch between solar, battery, and generator power with intelligent...</p>
    <span class="arrow-dot"><svg width="12" height="12"><path d="M2 10L10 2M4 2h6v6" stroke="#fa4616" stroke-width="1.6" fill="none"/></svg></span>
  </div>
  <div class="solution" style="left:614px">
    <div class="icon" role="img" aria-label="Lithium battery" style="background:linear-gradient(#3a95e0,#1c6cc0)"></div>
    <h4>Lithium Batteries</h4><p>Long-lasting, high-performance Pinewatt lithium batteries store energy...</p>
    <span class="arrow-dot"><svg width="12" height="12"><path d="M2 10L10 2M4 2h6v6" stroke="#fff" stroke-width="1.6" fill="none"/></svg></span>
  </div>
  <div class="solution" style="left:862px">
    <div class="icon" role="img" aria-label="Future energy technology" style="background:linear-gradient(#d4532a,#7a2a12);width:44px"></div>
    <h4>Future Technologies</h4><p>We're continuously innovating! Soon, we'll introduce small windmills...</p>
    <span class="arrow-dot"><svg width="12" height="12"><path d="M2 10L10 2M4 2h6v6" stroke="#fff" stroke-width="1.6" fill="none"/></svg></span>
  </div>
</section>

<section class="why">
  <h2 class="abs" style="left:139px;top:2105px;font-size:34px">Why Choose Us?</h2>
  <div class="why-item" style="top:2150px">
    <svg class="why-icon" viewBox="0 0 52 52"><circle cx="26" cy="26" r="16" fill="none" stroke="#8df25c" stroke-width="2"/><ellipse cx="26" cy="26" rx="7" ry="16" fill="none" stroke="#8df25c" stroke-width="2"/><path d="M10 26h32M13 18h26M13 34h26" stroke="#8df25c" stroke-width="2"/></svg>
    <div><h4>Global Reach</h4><p>We supply worldwide with fast shipping</p></div>
  </div>
  <div class="why-item" style="top:2236px">
    <svg class="why-icon" viewBox="0 0 52 52"><circle cx="26" cy="16" r="9" fill="none" stroke="#8df25c" stroke-width="2"/><path d="M6 38c8-4 14-4 20 0l12-8 6 4-18 12-20-4z" fill="none" stroke="#8df25c" stroke-width="2"/></svg>
    <div><h4>Top Brands</h4><p>We offer Koru, Pinewatt, and Lumask Energy products.</p></div>
  </div>
  <div class="why-item" style="top:2322px">
    <svg class="why-icon" viewBox="0 0 52 52"><circle cx="26" cy="28" r="16" fill="none" stroke="#8df25c" stroke-width="2"/><path d="M19 28l5 5 10-10" stroke="#8df25c" stroke-width="2.4" fill="none"/><path d="M22 8h8" stroke="#8df25c" stroke-width="2"/></svg>
    <div><h4>Future-Ready</h4><p>Expanding into small windmills and hydropower.</p></div>
  </div>
  <div class="why-item" style="top:2408px">
    <svg class="why-icon" viewBox="0 0 52 52"><circle cx="26" cy="26" r="18" fill="none" stroke="#8df25c" stroke-width="2" stroke-dasharray="4 3"/><circle cx="26" cy="26" r="9" fill="none" stroke="#8df25c" stroke-width="2"/></svg>
    <div><h4>Seamless Shopping</h4><p>A secure webshop with international payments.</p></div>
  </div>
  <div class="abs ph" role="img" aria-label="Wall-mounted hybrid inverter" style="left:652px;top:2087px;width:400px;height:417px;background:linear-gradient(135deg,#fde3d9 0%,#f5f5f5 25%,#e2e2e2 70%,#2a2a2a 100%)"></div>
  <div class="abs" style="left:90px;right:90px;top:2573px;border-top:1px solid var(--line)"></div>
</section>

<section class="steps">
  <h2 class="section-title abs" style="top:2630px;left:0;width:1200px">How Installation Works</h2>
  <div class="step-num" style="left:160px;top:2722px">01</div>
  <div class="step-num" style="left:355px;top:2883px">02</div>
  <div class="step-num" style="left:548px;top:2722px">03</div>
  <div class="step-num" style="left:744px;top:2883px">04</div>
  <div class="step-num" style="left:937px;top:2722px">05</div>
  <svg class="abs" style="left:0;top:2780px" width="1200" height="140">
    <g stroke="#fa4616" stroke-width="2" fill="none">
      <path d="M282 70 C300 120 330 125 352 120"/><path d="M343 113l9 7-10 4"/>
      <path d="M478 120 C510 110 535 80 540 55"/><path d="M532 62l8-8 4 10"/>
      <path d="M672 70 C690 120 720 125 742 120"/><path d="M733 113l9 7-10 4"/>
      <path d="M867 120 C900 110 925 80 930 55"/><path d="M922 62l8-8 4 10"/>
    </g>
  </svg>
  <div class="step-text" style="left:114px;top:2864px"><h4>Consultation<br>&amp; System Design</h4><p>Our experts assess your energy needs and recommend the best solution.</p></div>
  <div class="step-text" style="left:309px;top:2752px"><h4>Product Selection<br>&amp; Purchase</h4><p>Choose from our top-tier brands and place your order via our secure webshop.</p></div>
  <div class="step-text" style="left:503px;top:2864px"><h4>Delivery &amp;<br>Setup Guidance</h4><p>We ship worldwide with detailed installation guides and remote support.</p></div>
  <div class="step-text" style="left:698px;top:2752px"><h4>Professional<br>Installation</h4><p>Need expert assistance? We can connect you with certified installers in your area.</p></div>
  <div class="step-text" style="left:891px;top:2864px"><h4>Ongoing<br>Support</h4><p>Monitor performance and optimize usage with our guidance and technical support.</p></div>
</section>

<section class="reviews">
  <h2 class="section-title abs" style="top:3138px;left:0;width:1200px">What Our Customers Say</h2>
  <div class="review" style="left:90px"><div class="who"><div class="avatar" role="img" aria-label="Customer portrait"></div><div><strong>Jorin V.</strong><span class="stars">★★★★<span style="color:#ddd">★</span></span></div></div><p>It is a long established fact that a reader will be distracted by the readable content of a page when looking at its layout. It is a long...</p></div>
  <div class="review featured" style="left:529px"><div class="who"><div class="avatar" role="img" aria-label="Customer portrait"></div><div><strong>Lena M.</strong><span class="stars">★★★★<span style="color:#fff">★</span></span></div></div><p>It is a long established fact that a reader will be distracted by the readable content of a page when looking at its layout. It is a long...</p></div>
  <div class="review" style="left:962px"><div class="who"><div class="avatar" role="img" aria-label="Customer portrait"></div><div><strong>Pieter S.</strong><span class="stars">★★★★<span style="color:#ddd">★</span></span></div></div><p>It is a long established fact that a reader will be distracted by the readable content of a page when looking at its layout.</p></div>
  <div class="dots"><span></span><span></span><span></span></div>
  <div class="abs" style="left:90px;right:90px;top:3551px;border-top:1px solid var(--line)"></div>
</section>

<section class="contact">
  <form class="contact-card">
    <h2>GET IN TOUCH</h2>
    <div class="field">First Name</div>
    <div class="field">Last Name</div>
    <div class="field">Email Address</div>
    <div class="field">Phone Number</div>
    <div class="field tall">How Can We Help You?</div>
    <button class="submit" type="button">SUBMIT</button>
  </form>
  <h2 class="abs" style="left:646px;top:3768px;font-size:33px;line-height:42px">LET'S POWER<br>YOUR FUTURE!</h2>
  <p class="abs" style="left:646px;top:3868px;width:420px;font-size:13px;line-height:22px;color:var(--text)">Not sure what you need? Our expert team is ready to help. Contact us for personalized recommendations and solutions tailored to your energy needs.</p>
  <a class="btn btn-orange abs" style="left:646px;top:3960px;height:48px;padding:0 30px">Contact Us</a>
</section>

<footer class="site-footer">
  <div class="abs" style="left:170px;top:185px;display:flex;align-items:center;gap:12px"><span style="width:30px;height:30px;background:var(--orange)"></span><span style="font:700 30px var(--body);color:var(--white)">Vormsted</span></div>
  <div class="footer-col" style="left:466px"><h4>Quick Links</h4><ul><li>Home</li><li>About Us</li><li>Products</li><li>Contact Us</li></ul></div>
  <div class="footer-col" style="left:673px"><h4>Information</h4><ul><li>Privacy Policy</li><li>Disclaimer</li><li>Terms &amp; Condition</li><li>Site Map</li></ul></div>
  <div class="footer-col info" style="left:887px"><h4>Information</h4><ul>
    <li><span style="color:var(--orange)">✉</span> Email:<br>&nbsp;&nbsp;&nbsp;&nbsp;hello@vormsted.example</li>
    <li><span style="color:var(--orange)">☎</span> Phone:<br>&nbsp;&nbsp;&nbsp;&nbsp;+012 480 3917<br>&nbsp;&nbsp;&nbsp;&nbsp;+012 480 3918</li></ul>
    <div class="social"><span></span><span></span></div></div>
  <div class="copyright">© COPYRIGHT 2025 VORMSTED, ALL RIGHTS RESERVED</div>
  <span class="to-top"><svg width="14" height="10"><path d="M1 9l6-7 6 7" stroke="#fff" stroke-width="2" fill="none"/></svg></span>
</footer>

</body>
</html>
```